new ownership of a business

Tax & accounting firm including payroll processing, business consulting, bookkeeping
I am a new owner and want to inform current clients I want the announcement to be subtle. something like "same friendly faces, brand new name" the name is going from "Wendell R. Pickett, CPA, PC" to "Pickett Marlowe & Associates, LLC" I would like to emphasize a little on the Marlowe part of the name. I would like the words "Tax Accountants" below the name.
Accounting

```html
<!DOCTYPE html>
<html lang="en">
<head>
<meta charset="utf-8">
<title>Pickett Marlowe &amp; Associates – Postcard</title>
<link rel="stylesheet" href="https://fonts.googleapis.com/css2?family=Open+Sans:ital,wght@0,400;0,600;1,400;1,600&family=Tinos:wght@400&display=swap">
<style>
  :root {
    --page-bg: #ece7df;
    --paper: #ffffff;
    --brand-red: #8b0000;
    --bright-red: #e3141b;
    --ink: #111111;
    --rule: #8a8a8a;
    --cream: #f3edc6;
    --photo-dark: #3d4048;
    --photo-light: #d9dadd;
    --sans: "Open Sans", Arial, sans-serif;
    --serif: "Tinos", "Times New Roman", serif;
  }
  * { box-sizing: border-box; margin: 0; padding: 0; }
  html, body { width: 775px; height: 1200px; overflow: hidden; }
  body { background: var(--page-bg); position: relative; font-family: var(--sans); }

  .postcard { position: absolute; left: 36px; width: 691px; background: var(--paper); overflow: hidden; }
  .postcard--front { top: 15px; height: 535px; }
  .postcard--back { top: 620px; height: 534px; }

  /* Front */
  .hero-photo {
    position: absolute; inset: 0;
    background: linear-gradient(115deg, var(--photo-dark) 0%, #6b6e76 55%, var(--photo-light) 100%);
  }
  .front-art { position: absolute; inset: 0; width: 100%; height: 100%; }
  .kicker {
    position: absolute; left: 22px; top: 26px;
    font-style: italic; font-weight: 400; font-size: 34px; color: var(--brand-red); letter-spacing: 0.5px;
  }
  .headline {
    position: absolute; right: 20px; top: 84px; text-align: right;
    font-size: 37px; line-height: 38px; font-weight: 400; color: var(--ink);
  }
  .headline em { font-style: italic; color: var(--brand-red); }
  .headline .line1 { margin-right: 13px; }

  .name-card {
    position: absolute; left: 276px; top: 214px; width: 251px; height: 161px;
    background: #f7f7f9; transform: rotate(-2deg);
    box-shadow: 0 2px 6px rgba(0,0,0,0.35);
    text-align: center; padding-top: 22px;
  }
  .name-card .old-name { font-size: 15px; color: var(--ink); }
  .name-card .arrow { display: block; margin: 6px auto 4px; }
  .name-card .new-name { font-size: 15.5px; font-style: italic; color: var(--brand-red); }
  .name-card .new-name strong { font-weight: 600; }
  .name-card .tagline { font-size: 15px; font-style: italic; color: var(--brand-red); }

  /* Back */
  .desk-photo {
    position: absolute; left: 0; top: 0; width: 333px; height: 211px;
    background: linear-gradient(180deg, #d6d8de 0%, #eeeef0 60%, #b9bbc0 100%);
  }
  .services-band {
    position: absolute; left: 0; top: 211px; width: 333px; height: 37px;
    background: var(--brand-red); color: #fff; font-family: var(--serif); font-size: 26px;
    padding-left: 29px; line-height: 37px;
  }
  .services-list { position: absolute; left: 40px; top: 252px; list-style: none; }
  .services-list li { font-family: var(--serif); font-size: 23.5px; line-height: 29px; color: var(--brand-red); }
  .services-list li::before { content: "●"; color: var(--bright-red); font-size: 13px; margin-right: 5px; vertical-align: 3px; }
  .services-rule { position: absolute; left: 0; top: 385px; width: 333px; height: 5px; background: var(--brand-red); }

  .return-address {
    position: absolute; left: 346px; top: 46px; font-style: normal;
    font-family: var(--serif); font-size: 16px; line-height: 20.5px; color: var(--bright-red);
  }
  .stamp-box { position: absolute; left: 570px; top: 16px; width: 104px; height: 103px; border: 1px solid #b5b5b5; }
  .address-line { position: absolute; left: 381px; width: 278px; height: 1px; background: var(--rule); }
  .address-line--1 { top: 264px; }
  .address-line--2 { top: 306px; }
  .address-line--3 { top: 349px; }
  .address-line--4 { top: 391px; }
</style>
</head>
<body>

<section class="postcard postcard--front">
  <div class="hero-photo" role="img" aria-label="Photo placeholder: businessman in a suit holding out a business card"></div>
  <svg class="front-art" viewBox="0 0 691 535" aria-hidden="true">
    <path d="M0 0 H691 V70 C560 0 360 10 0 160 Z" fill="var(--cream)" opacity="0.95"/>
    <path d="M0 158 C250 50 470 10 691 40" fill="none" stroke="#2a2418" stroke-width="3"/>
    <path d="M0 168 C260 60 480 25 691 55" fill="none" stroke="#c8b98a" stroke-width="2"/>
    <path d="M0 485 C200 420 420 390 691 400 V535 H0 Z" fill="var(--brand-red)" opacity="0.85"/>
    <path d="M0 475 C220 410 450 380 691 395" fill="none" stroke="var(--bright-red)" stroke-width="4"/>
    <path d="M0 490 C230 420 460 395 691 410" fill="none" stroke="#f0484e" stroke-width="2"/>
    <path d="M0 500 C250 440 470 410 691 425" fill="none" stroke="#b01010" stroke-width="2"/>
  </svg>
  <div class="kicker">Latest News!</div>
  <h1 class="headline">
    <span class="line1">Same <em>friendly faces,</em></span><br>
    <span class="line2">Brand <em>new name!!</em></span>
  </h1>
  <div class="name-card">
    <div class="old-name">Wendell R. Pickett, CPA, PC</div>
    <svg class="arrow" width="48" height="30" viewBox="0 0 48 30" aria-hidden="true">
      <path d="M4 2 L24 14 L44 2 L44 8 L24 20 L4 8 Z" fill="#111"/>
      <path d="M4 12 L24 24 L44 12 L44 18 L24 30 L4 18 Z" fill="#111"/>
    </svg>
    <div class="new-name">Pickett <strong>Marlowe</strong> &amp; Associates, LLC</div>
    <div class="tagline">Tax Accountants</div>
  </div>
</section>

<section class="postcard postcard--back">
  <div class="desk-photo" role="img" aria-label="Photo placeholder: hands reviewing a financial spreadsheet beside a calculator"></div>
  <div class="services-band">Our Services</div>
  <ul class="services-list">
    <li>Tax &amp; accounting</li>
    <li>Payroll Processing</li>
    <li>Business Consulting</li>
    <li>Bookkeeping</li>
  </ul>
  <div class="services-rule"></div>

  <address class="return-address">
    Pickett Marlowe &amp; Associates,<br>LLC<br>Tax Accountants
  </address>
  <div class="stamp-box"></div>
  <div class="address-line address-line--1"></div>
  <div class="address-line address-line--2"></div>
  <div class="address-line address-line--3"></div>
  <div class="address-line address-line--4"></div>
</section>

</body>
</html>
```